I need a business card design for a new counselling practice in Canberra, Australia. The name of the practice is Dr Grant Holloway, Counselling Services and the practice focuses on philosophical, narrative and existential counselling for individuals, couples and families. The final design should communicate professionalism, sophistication of analysis and psychological wholeness. The reverse side of the card should have an appointment reminder

Could the following qualifications also be included on card. BSc (Psychology), BA hons (Philosophy), PhD (Philosophy), Diploma of Community Counselling And the following affiliation Wellspring Guild of Talk Therapists and Allied Carers Inc. (WEGOTAC) And my contact phone mobile phone number is 0493817254, and email is Grant.Holloway347@mailbox-example.net for inclusion as well.

Thank you all who have put in a design so far. I just wanted to clarify some design points based on what you have submitted. 1. The Wellspring Guild of Talk Therapists. Allied Carers Inc. (WEGOTAC) is an affiliation only. 'Member of the Wellspring Guild of Talk Therapists. Allied Carers Inc (WEGOTAC)' should appear with the same prominence of a qualification. 2. The Post Graduate Diploma in Community Counselling is a quaification and should appear as 'PG Dip (Community Counselling)' after the other qualifications. 3. I am advertising myself as a counsellor so 'Dr Grant Holloway, Counselling Services' or 'Dr Grant Holloway, Counsellor' is the equivalent of the business name. After looking at some of the designs I prefer Dr Grant Holloway in sentence case rather than all capitals (DR GRANT HOLLOWAY). 4. 'Philosophical, narrative and existential counselling for individuals, couples and families' is the description of the type of counselling services and should appear on the card.

One further point. I have updated my email address for the card. It is now drgrantholloway@tallowfieldtherapy.org

```html
<!DOCTYPE html>
<html lang="en">
<head>
<meta charset="utf-8">
<title>Dr Grant Holloway – Counselling Services business card</title>
<link rel="stylesheet" href="https://fonts.googleapis.com/css2?family=Tinos:wght@400&family=Source+Sans+3:wght@400;600&display=swap">
<style>
  :root {
    --backdrop: #a9a9a9;
    --card: #ffffff;
    --brand-blue: #2d50a0;
    --band-top: #2f58b0;
    --band-bottom: #213f86;
    --slate: #555a60;
    --soft-grey: #7a7d82;
    --faint: #eeeeee;
    --dots: #8a8a8a;
  }
  * { margin: 0; padding: 0; box-sizing: border-box; }
  html, body { width: 1200px; height: 900px; overflow: hidden; }
  body {
    background: var(--backdrop);
    font-family: "Source Sans 3", sans-serif;
    position: relative;
  }
  .card {
    position: absolute;
    top: 290px;
    width: 530px;
    height: 320px;
    background: var(--card);
    border-radius: 24px;
    overflow: hidden;
    box-shadow: 0 6px 18px rgba(0,0,0,0.18);
  }
  .card--front { left: 50px; }
  .card--back { left: 620px; }

  /* Front */
  .front-band { position: absolute; left: 0; bottom: 0; width: 100%; height: 145px; }
  .brand-mark {
    position: absolute; left: 50%; top: 18px; transform: translateX(-50%);
    width: 72px; height: 72px; border-radius: 50%;
    border: 6px solid var(--slate); background: var(--brand-blue);
  }
  .practice-name {
    position: absolute; left: 0; right: 0; top: 100px; text-align: center;
    font-family: "Tinos", serif; font-weight: 400; font-size: 34px; color: var(--brand-blue); line-height: 1;
  }
  .practice-tagline {
    position: absolute; left: 0; right: 0; top: 137px; text-align: center;
    font-family: "Tinos", serif; font-size: 9px; letter-spacing: 4.5px; color: var(--slate); line-height: 1;
  }
  .qualifications {
    position: absolute; left: 0; right: 0; top: 153px; text-align: center;
    font-size: 9px; line-height: 1.2; color: var(--brand-blue);
  }
  .contact {
    position: absolute; left: 0; right: 0; bottom: 24px; text-align: center; color: #fff;
  }
  .contact__phone { font-size: 21px; line-height: 1.2; }
  .contact__email { font-size: 16px; line-height: 1.3; }

  /* Back */
  .faint-ring {
    position: absolute; left: 130px; top: -8px; width: 330px; height: 330px;
    border-radius: 50%; border: 16px solid var(--faint);
  }
  .appointments-title {
    position: absolute; left: 0; right: 0; top: 56px; text-align: center;
    font-size: 17px; font-weight: 400; color: var(--brand-blue);
    text-decoration: underline; text-underline-offset: 3px;
  }
  .field {
    position: absolute; display: flex; align-items: flex-end;
    font-size: 16px; font-weight: 600; color: var(--slate);
  }
  .field__label { white-space: nowrap; margin-right: 4px; }
  .field__line { flex: 1; border-bottom: 1.5px dotted var(--dots); height: 14px; margin-bottom: 4px; }
  .field--name { left: 30px; right: 24px; top: 100px; }
  .field--date { left: 30px; width: 220px; top: 140px; }
  .field--time { left: 280px; right: 24px; top: 130px; font-size: 14px; font-weight: 400; }
  .back-brand {
    position: absolute; right: 22px; bottom: 58px; display: flex; align-items: center; gap: 6px;
  }
  .back-brand__mark {
    width: 34px; height: 34px; border-radius: 50%;
    border: 3px solid var(--slate); background: var(--brand-blue);
  }
  .back-brand__name { font-family: "Tinos", serif; font-size: 19px; color: var(--brand-blue); line-height: 1; }
  .back-brand__tagline { font-family: "Tinos", serif; font-size: 5.5px; letter-spacing: 2.2px; color: var(--slate); }
</style>
</head>
<body>

<section class="card card--front">
  <svg class="front-band" viewBox="0 0 530 145" preserveAspectRatio="none" aria-hidden="true">
    <defs>
      <linearGradient id="bandFill" x1="0" y1="0" x2="0" y2="1">
        <stop offset="0" stop-color="#2f58b0"/>
        <stop offset="1" stop-color="#213f86"/>
      </linearGradient>
    </defs>
    <path d="M0 8 Q 200 72 530 52 L530 145 L0 145 Z" fill="url(#bandFill)"/>
    <path d="M0 2 Q 200 64 530 46" fill="none" stroke="#7a7d82" stroke-width="5"/>
  </svg>
  <div class="brand-mark" aria-hidden="true"></div>
  <h1 class="practice-name">Dr Grant Holloway</h1>
  <p class="practice-tagline">COUNSELLING SERVICES</p>
  <p class="qualifications">
    BSc (Psychology)&nbsp; BA hons (Philosophy)&nbsp; PhD (Philosophy)<br>
    PG Dip (Community Counselling)<br>
    Member of WEGOTAC<br>
    Philosophical, narrative and existential counselling for individuals, couples and families
  </p>
  <div class="contact">
    <p class="contact__phone">0493 817 254</p>
    <p class="contact__email">drgrantholloway@tallowfieldtherapy.org</p>
  </div>
</section>

<section class="card card--back">
  <div class="faint-ring" aria-hidden="true"></div>
  <h2 class="appointments-title">Appointments</h2>
  <div class="field field--name"><span class="field__label">Name :</span><span class="field__line"></span></div>
  <div class="field field--date"><span class="field__label">Date :</span><span class="field__line"></span></div>
  <div class="field field--time"><span class="field__label">Time :</span><span class="field__line"></span></div>
  <div class="back-brand">
    <div class="back-brand__mark" aria-hidden="true"></div>
    <div>
      <p class="back-brand__name">Dr Grant Holloway</p>
      <p class="back-brand__tagline">COUNSELLING SERVICES</p>
    </div>
  </div>
</section>

</body>
</html>
```